Biz Card for Harrowfield Property Partners - HFPP

Harrowfield Property Partners is a commercial real estate acquisitions firm. We buy commercial property and need to raise capital from investors for each deal we buy. The vibe needs to be: give us your money, we will multiply it.
Our website: www.hfldpp.com
Competitors are: https://marvenby.com/, https://trellumpartners.com/, http://www.quorvantcapital.com/
Target Market(s)
High Net Worth Individuals, Bankers, Insurance Companies, Commercial Real Estate Brokers.
Industry/Entity Type
Investment Banking
Contact Information for Business Card
Name, Title, Addess, Cell#, Office#, email, website
Requirements
Must have
- use one of our logos. See website for look and feel: www.hfldpp.com
Nice to have
- see website: www.hfldpp.com

```html
<!DOCTYPE html>
<html lang="en">
<head>
<meta charset="utf-8">
<title>Harrowfield Property Partners – Business Card</title>
<link rel="stylesheet" href="https://fonts.googleapis.com/css2?family=Montserrat:wght@400;500&family=Roboto:wght@400;700&display=swap">
<style>
  :root {
    --navy: #062340;
    --ink: #1d1d1f;
    --paper: #ffffff;
    --text-grey: #3a3a3a;
    --backdrop: #2a2a2b;
  }
  * { box-sizing: border-box; margin: 0; padding: 0; }
  html, body { width: 1200px; height: 1000px; overflow: hidden; }
  body { background: var(--backdrop); position: relative; font-family: "Roboto", sans-serif; }

  .card {
    position: absolute;
    width: 720px;
    height: 410px;
    border-radius: 22px;
    overflow: hidden;
    box-shadow: 0 12px 30px rgba(0,0,0,.45);
  }

  /* Front */
  .card--front { left: 420px; top: 50px; background: var(--navy); }
  .front-mark {
    position: absolute; inset: 0;
    display: flex; flex-direction: column; align-items: center; justify-content: center; gap: 22px;
  }
  .front-mark .mark-circle {
    width: 120px; height: 120px; border-radius: 50%; background: var(--paper);
  }
  .front-mark .brand-name {
    font-family: "Montserrat", sans-serif; font-weight: 500;
    color: var(--paper); font-size: 30px; letter-spacing: 6px;
    text-transform: uppercase; text-align: center; line-height: 1.35;
  }

  /* Back */
  .card--back { left: 80px; top: 520px; background: var(--paper); }
  .back-wave { position: absolute; left: 0; bottom: 0; width: 720px; height: 410px; }

  .back-mark {
    position: absolute; left: 30px; top: 70px; width: 300px;
    display: flex; flex-direction: column; align-items: center; gap: 16px;
  }
  .back-mark .mark-circle {
    width: 92px; height: 92px; border-radius: 50%; background: var(--navy);
  }
  .back-mark .brand-name {
    font-family: "Montserrat", sans-serif; font-weight: 500;
    color: var(--navy); font-size: 21px; letter-spacing: 4px;
    text-transform: uppercase; text-align: center; line-height: 1.35;
  }

  .divider {
    position: absolute; left: 350px; top: 60px; width: 1px; height: 210px; background: var(--navy);
  }

  .contact { position: absolute; left: 378px; top: 62px; color: var(--text-grey); }
  .contact .person-name { font-weight: 700; font-size: 25px; color: var(--navy); letter-spacing: .5px; }
  .contact .person-title { font-size: 17px; margin-bottom: 6px; }
  .contact .address { font-size: 17px; line-height: 1.3; margin-bottom: 6px; }
  .contact ul { list-style: none; }
  .contact li { display: flex; align-items: center; gap: 8px; font-size: 17px; line-height: 1.4; }
  .contact svg { width: 14px; height: 14px; fill: var(--navy); flex: none; }
</style>
</head>
<body>

<section class="card card--front" aria-label="Card front">
  <div class="front-mark">
    <div class="mark-circle"></div>
    <div class="brand-name">Harrowfield<br>Property Partners</div>
  </div>
</section>

<section class="card card--back" aria-label="Card back">
  <svg class="back-wave" viewBox="0 0 720 410" preserveAspectRatio="none" aria-hidden="true">
    <path d="M0 250 C 160 330, 420 380, 720 380 L720 410 L0 410 Z" fill="var(--navy)"/>
    <path d="M230 335 C 380 372, 560 384, 720 372 L720 382 C 560 392, 380 382, 230 335 Z" fill="var(--ink)"/>
    <path d="M238 336 C 390 376, 560 388, 720 380" fill="none" stroke="var(--paper)" stroke-width="2"/>
  </svg>

  <div class="back-mark">
    <div class="mark-circle"></div>
    <div class="brand-name">Harrowfield<br>Property Partners</div>
  </div>

  <div class="divider"></div>

  <div class="contact">
    <p class="person-name">DALTON REEVE</p>
    <p class="person-title">Owner/Founder</p>
    <p class="address">3180 Larkmoor Ave. 620<br>Westbrook Falls 04</p>
    <ul>
      <li><svg viewBox="0 0 24 24"><path d="M6.6 10.8a15.1 15.1 0 0 0 6.6 6.6l2.2-2.2c.3-.3.7-.4 1-.2 1.1.4 2.3.6 3.6.6.6 0 1 .4 1 1V20c0 .6-.4 1-1 1A17 17 0 0 1 3 4c0-.6.4-1 1-1h3.5c.6 0 1 .4 1 1 0 1.3.2 2.5.6 3.6.1.3 0 .7-.2 1z"/></svg>555-018-2741</li>
      <li><svg viewBox="0 0 24 24"><path d="M7 1h10a2 2 0 0 1 2 2v18a2 2 0 0 1-2 2H7a2 2 0 0 1-2-2V3a2 2 0 0 1 2-2zm0 3v14h10V4zm5 15.2a1 1 0 1 0 0 2 1 1 0 0 0 0-2z"/></svg>555-014-9362</li>
      <li><svg viewBox="0 0 24 24"><path d="M2 5h20v14H2zm2 2v.4l8 5.2 8-5.2V7zm0 2.8V17h16V9.8l-8 5.2z"/></svg>info@hfldpp.com</li>
      <li><svg viewBox="0 0 24 24"><path d="M12 2a10 10 0 1 0 0 20 10 10 0 0 0 0-20zm6.9 9h-3a15 15 0 0 0-1.3-5.6A8 8 0 0 1 18.9 11zM12 4c.9 1.2 1.7 3.6 1.9 7h-3.8c.2-3.4 1-5.8 1.9-7zM9.4 5.4A15 15 0 0 0 8.1 11h-3a8 8 0 0 1 4.3-5.6zM5.1 13h3a15 15 0 0 0 1.3 5.6A8 8 0 0 1 5.1 13zM12 20c-.9-1.2-1.7-3.6-1.9-7h3.8c-.2 3.4-1 5.8-1.9 7zm2.6-1.4a15 15 0 0 0 1.3-5.6h3a8 8 0 0 1-4.3 5.6z"/></svg>www.hfldpp.com</li>
    </ul>
  </div>
</section>

</body>
</html>
```